Website Design For Atelier Nine Design Group

Create a sophisticated website that denotes high-end luxury. We would like to keep the copy minimalist and elegantly understated while communicating only the most essential information. While creating an air of exclusivity.
We would like 3-4 Tab Wesbite
Home:
• Feature a design project front and centre, along with a short
introduction about who we are and what we do.

We can put a Call To Action at the end of the introduction inviting readers to learn more on our About page.
About:
• This page should provide more detail on our background, past
achievements, history of the company, and anything you'd like to
highlight.
• We should also provide details on our services, aesthetic, process, etc.
Team:
• introduce the team, possibly with short descriptions for each
team member. Total Team Members 7
Residential
• The portfolio page can be a grid of images along with titles for
each project.
• Clicking on each image should take you to a separate page for that
project where readers can find more details

Commercial
The portfolio page can be a grid of images along with titles for
each project.

Contact Us:

example website:
https://www.venkorahinteriors.example/

Target Market(s)

High end luxury clientele

Industry/Entity Type

Interior Design

Number of Pages Required

4 page

Font styles to use
Sans Serif

Requirements
Must have
• Company logo, color scheme and name: Atelier Nine Design Group

```html
<!DOCTYPE html>
<html lang="en">
<head>
<meta charset="utf-8">
<title>Atelier Nine Design Group</title>
<link href="https://fonts.googleapis.com/css2?family=Figtree:wght@500;600;700;800&family=Lato:wght@400;700&display=swap" rel="stylesheet">
<style>
:root{
  --gold:#c4a240;
  --gold-dark:#a08430;
  --navy:#13394a;
  --teal:#1c4a48;
  --ink:#111;
  --text:#333;
  --white:#fff;
  --footer:#000;
}
*{box-sizing:border-box;margin:0;padding:0}
html,body{width:754px;height:1200px;overflow:hidden;background:var(--white)}
body{position:relative;font-family:"Lato",sans-serif;color:var(--text)}
.abs{position:absolute}
/* header */
.brand{left:82px;top:8px;width:70px;text-align:center;color:var(--navy);font-family:"Figtree",sans-serif;font-weight:800;display:flex;align-items:center;gap:4px}
.brand-mark{width:8px;height:8px;background:var(--gold);flex:none}
.brand-name{font-size:12px;line-height:1.05;letter-spacing:.5px;text-align:left}
.brand-name small{display:block;font-size:6px;letter-spacing:1.2px}
.nav{top:15px;left:0;font-family:"Figtree",sans-serif;font-weight:600;font-size:8.5px;color:var(--ink)}
.nav a{position:absolute;white-space:nowrap;color:inherit;text-decoration:none}
.nav a.active{color:var(--gold)}
.cart{left:640px;top:8px;width:26px;height:26px;border-radius:50%;background:linear-gradient(135deg,var(--gold),var(--navy))}
.badge{left:660px;top:8px;width:9px;height:9px;border-radius:50%;background:#e01010;color:#fff;font-size:6px;text-align:center;line-height:9px;font-weight:700}
/* hero */
.hero-panel{top:46px;height:366px}
.hero-left{left:0;width:373px;border-radius:0 14px 14px 0;background:linear-gradient(135deg,#8d8e92 0%,#b9bbc0 40%,#e6e8ee 60%,#7a736c 100%)}
.hero-right{left:380px;width:374px;border-radius:14px 0 0 14px;background:linear-gradient(160deg,#9a5a30 0%,#5d3a22 35%,#2a2520 65%,#4a3d32 100%)}
.ribbon{top:216px;height:26px;color:#fff;font-family:"Figtree",sans-serif;font-weight:700;font-size:8.5px;line-height:26px}
.ribbon-res{left:170px;width:180px;background:linear-gradient(90deg,var(--gold),#8a7630);clip-path:polygon(7% 0,100% 0,100% 100%,7% 100%,0 50%)}
.ribbon-com{left:405px;width:180px;background:linear-gradient(90deg,#2c5a4a,var(--navy));clip-path:polygon(0 0,93% 0,100% 50%,93% 100%,0 100%)}
.hex{left:337px;top:193px}
/* welcome */
.title{top:463px;width:754px;text-align:center;font-family:"Figtree",sans-serif;font-weight:700;font-size:23px;color:var(--ink)}
.rule{top:496px;height:3px;width:27px}
.kicker{width:754px;text-align:center;font-family:"Figtree",sans-serif;font-weight:700;font-size:9.5px;color:var(--gold)}
.intro{left:108px;top:546px;width:538px;font-size:10px;line-height:17.5px;text-align:justify;text-align-last:center}
.card{top:668px;width:284px;height:207px;border-radius:5px;overflow:hidden}
.card-res{left:88px;background:linear-gradient(180deg,#d9d4c7 0%,#c8b990 45%,#c9a84a 100%)}
.card-com{left:382px;background:linear-gradient(180deg,#7a756c 0%,#4a4744 50%,#2a2826 100%)}
.card-frame{position:absolute;inset:9px 11px 9px 11px;border:1.5px solid rgba(255,255,255,.9);border-radius:4px}
.card-label{position:absolute;left:0;right:0;top:154px;text-align:center;color:#fff;font-family:"Figtree",sans-serif;font-weight:700;font-size:16.5px}
.cta{left:321px;top:908px;width:112px;height:35px;border-radius:18px;background:linear-gradient(90deg,var(--gold),var(--navy));color:#fff;font-family:"Figtree",sans-serif;font-weight:700;font-size:9.5px;line-height:35px;text-align:center}
/* footer */
.footer{left:0;top:989px;width:754px;height:211px;background:var(--footer);color:#fff}
.fh{top:44px;font-family:"Figtree",sans-serif;font-weight:700;font-size:9.5px}
.flist{list-style:none;font-size:7.7px;line-height:17.5px}
.flist li::before{content:"»";margin-right:6px;font-size:8px}
.contact{font-size:7.7px}
.contact svg{position:absolute;left:-16px;top:0}
.fbrand{left:540px;top:42px;width:124px;text-align:center;font-family:"Figtree",sans-serif;font-weight:800;color:#fff}
.fbrand .sq{width:14px;height:14px;background:var(--gold);margin:0 auto 8px}
.fbrand .n{font-size:19px;letter-spacing:1.5px;line-height:1}
.fbrand .g{font-size:8px;letter-spacing:2.5px;margin-top:5px}
.social{top:1120px;width:19px;height:19px;border-radius:50%;background:linear-gradient(135deg,var(--gold),var(--teal))}
.divider{left:84px;top:1150px;width:588px;height:1px;background:#bbb}
.copy{top:1160px;width:754px;text-align:center;font-size:7.7px;color:#fff}
</style>
</head>
<body>
<header>
  <div class="abs brand"><span class="brand-mark"></span><span class="brand-name">ATELIER NINE<small>DESIGN GROUP</small></span></div>
  <nav class="abs nav">
    <a class="active" style="left:269px">HOME</a>
    <a style="left:317px">ABOUT</a>
    <a style="left:368px">TEAM</a>
    <a style="left:413px">RESIDENTIAL</a>
    <a style="left:487px">COMMERCIAL</a>
    <a style="left:565px">CONTACT US</a>
  </nav>
  <div class="abs cart">
    <svg width="26" height="26" viewBox="0 0 26 26"><path d="M8 9h2l1.5 6h5.5l1.5-4.5h-7.5" fill="none" stroke="#fff" stroke-width="1.5"/><circle cx="12" cy="17.5" r="1" fill="#fff"/><circle cx="16.5" cy="17.5" r="1" fill="#fff"/></svg>
  </div>
  <div class="abs badge">2</div>
</header>

<section class="hero">
  <div class="abs hero-panel hero-left" role="img" aria-label="Residential project: marble bathroom with freestanding tub"></div>
  <div class="abs hero-panel hero-right" role="img" aria-label="Commercial project: office with brick vaulted ceiling and desks"></div>
  <div class="abs ribbon ribbon-res">
    <svg class="abs" style="left:12px;top:9px" width="16" height="8" viewBox="0 0 16 8"><path d="M15 4H1M4 1L1 4l3 3" fill="none" stroke="#fff" stroke-width="1"/></svg>
    <span class="abs" style="left:47px">Residential</span>
  </div>
  <div class="abs ribbon ribbon-com">
    <span class="abs" style="left:82px">Commercial</span>
    <svg class="abs" style="left:153px;top:9px" width="16" height="8" viewBox="0 0 16 8"><path d="M1 4h14M12 1l3 3-3 3" fill="none" stroke="#fff" stroke-width="1"/></svg>
  </div>
  <svg class="abs hex" width="80" height="70" viewBox="0 0 80 70">
    <defs><linearGradient id="playGrad" x1="0" x2="1"><stop offset="0" stop-color="#c4a240"/><stop offset="1" stop-color="#13394a"/></linearGradient></defs>
    <polygon points="20,0 60,0 80,35 60,70 20,70 0,35" fill="#fff"/>
    <polygon points="31,23 52,35 31,47" fill="url(#playGrad)"/>
  </svg>
</section>

<section class="welcome">
  <h1 class="abs title">Welcome To Atelier Nine Design Group</h1>
  <div class="abs rule" style="left:349px;background:var(--gold)"></div>
  <div class="abs rule" style="left:378px;background:var(--navy)"></div>
  <h2 class="abs kicker" style="top:523px">WHO WE ARE</h2>
  <p class="abs intro">Lorem ipsum dolor sit amet, consectetur adipiscing elit, sed do eiusmod tempor incididunt ut labore et dolore magna aliqua. Quis ipsum suspendisse ultrices gravida. Risus commodo viverra maecenas accumsan lacus vel facilisis. perspiciatis unde omnis iste natus error sit voluptatem accusantium doloremque laudantium, totam rem aperiam, eaque ipsa quae ab illo inventore veritatis et quasi architecto beatae vitae dicta sunt explicabo.</p>
  <h2 class="abs kicker" style="top:639px">WHAT WE DO</h2>
  <div class="abs card card-res" role="img" aria-label="Residential living room with sofa and coffee table">
    <div class="card-frame"></div><div class="card-label">RESIDENTIAL</div>
  </div>
  <div class="abs card card-com" role="img" aria-label="Commercial office corner with desk and armchair">
    <div class="card-frame"></div><div class="card-label">COMMERCIAL</div>
  </div>
  <div class="abs cta">LEARN MORE</div>
</section>

<footer class="abs footer">
  <h3 class="abs fh" style="left:95px">QUICK LINKS</h3>
  <ul class="abs flist" style="left:94px;top:55px"><li>Home</li><li>About</li><li>Team</li><li>Residential</li><li>Commercial</li></ul>
  <h3 class="abs fh" style="left:231px">LEGAL</h3>
  <ul class="abs flist" style="left:228px;top:55px"><li>Terms of Use</li><li>Privacy Policy</li><li>Contact Us</li><li>FAQ</li></ul>
  <h3 class="abs fh" style="left:361px">CONTACT US</h3>
  <div class="abs contact" style="left:369px;top:60px;line-height:17.5px">
    <svg width="7" height="9" viewBox="0 0 7 9"><path d="M3.5 0A3.3 3.3 0 0 0 .2 3.3C.2 5.7 3.5 9 3.5 9s3.3-3.3 3.3-5.7A3.3 3.3 0 0 0 3.5 0z" fill="#fff"/><circle cx="3.5" cy="3.3" r="1.2" fill="#000"/></svg>
    123 Lorem ipsum dolor sit amet<br>&nbsp;consectetur adipisci.
  </div>
  <div class="abs contact" style="left:370px;top:102px">
    <svg width="8" height="8" viewBox="0 0 8 8"><path d="M1 .5l1.6-.3 1 2-1 .8a5 5 0 0 0 2.4 2.4l.8-1 2 1-.3 1.6C5 7.5.5 3 1 .5z" fill="#fff"/></svg>
    +1 888 888 8888
  </div>
  <div class="abs contact" style="left:371px;top:127px">
    <svg width="9" height="7" viewBox="0 0 9 7"><rect width="9" height="7" rx="1" fill="#fff"/><path d="M0 1l4.5 3L9 1" fill="none" stroke="#000" stroke-width=".8"/></svg>
    hello@ateliernine.example
  </div>
  <div class="abs fbrand"><div class="sq"></div><div class="n">ATELIER NINE</div><div class="g">DESIGN GROUP</div></div>
</footer>
<div class="abs social" style="left:546px"></div>
<div class="abs social" style="left:574px"></div>
<div class="abs social" style="left:601px"></div>
<div class="abs social" style="left:629px"></div>
<div class="abs divider"></div>
<p class="abs copy">© copyrights 2022 Atelier Nine Design Group &nbsp;| &nbsp;&nbsp; All rights reserved.</p>
</body>
</html>
```